Webdesign für Reittherapeutin
Zielgruppe
Ich bin Reittherapeutin und biete auf unserem privaten Hof Reittherapie für Kinder, Jugendliche und Erwachsene an. Die Therapieeinheiten finden im Freien statt, also auf dem Sandplatz oder im Gelände. In der Reittherapie steht nicht das Reiten, sonden der Umgang und die Beziehung zum Pferd im Vordergrund.
Aufgabenstellung
Mir gefallen Designs in Naturtönen, welche auch gut zu meiner Tätigkeit passen. Ich habe bereits ein Logo, einen Namen (Wiesen erleben) und die Domaine (www.wiesen-erleben.ch) ebenso.

```html
<!DOCTYPE html>
<html lang="de">
<head>
<meta charset="utf-8">
<title>Wiesen erleben – Reittherapie</title>
<link href="https://fonts.googleapis.com/css2?family=Fira+Sans+Condensed:wght@300;400&family=Varela+Round&family=Great+Vibes&display=swap" rel="stylesheet">
<style>
:root{
  --teal:#1a97a1;
  --brown:#7b6458;
  --brown-dark:#5f4a40;
  --paper:#ede9ea;
  --ink:#1d1d1d;
  --white:#ffffff;
  --black:#000000;
}
*{margin:0;padding:0;box-sizing:border-box}
html,body{width:1069px;height:1200px;overflow:hidden;background:var(--paper)}
body{position:relative;font-family:"Varela Round",sans-serif;color:var(--ink)}
.abs{position:absolute}

.sidebar{left:0;top:0;width:182px;height:1200px;background:var(--teal)}
.brand{left:0;top:0;width:182px;height:157px;background:var(--white);display:flex;flex-direction:column;align-items:center;justify-content:flex-end;padding-bottom:22px}
.brand-name{font-family:"Fira Sans Condensed",sans-serif;font-weight:300;font-size:25px;color:var(--brown-dark);letter-spacing:.3px}
.brand-tag{font-family:"Varela Round",sans-serif;font-size:8.5px;letter-spacing:3px;color:var(--teal);margin-top:4px}
.nav{left:0;top:212px;width:160px;list-style:none;text-align:center}
.nav li{height:47.8px;font-family:"Fira Sans Condensed",sans-serif;font-size:19px;color:var(--white)}

.hero{left:182px;top:0;width:887px;height:320px;background:linear-gradient(180deg,#8fb3de 0%,#b9cde6 34%,#9e9a7a 42%,#6f6450 62%,#3a2e2a 80%,#b3a58e 100%)}
.hero-title{left:672px;top:222px;font-family:"Fira Sans Condensed",sans-serif;font-weight:300;font-size:60px;letter-spacing:2px;color:#f1f1f1;line-height:1}
.hero-rule{left:676px;top:289px;width:252px;height:1px;background:var(--teal)}
.hero-sub{left:676px;top:294px;font-family:"Fira Sans Condensed",sans-serif;font-weight:300;font-size:14px;letter-spacing:1px;color:#eeeeee}

.intro{left:182px;top:320px;width:887px;height:319px;background:var(--paper)}
.intro-text{left:247px;top:387px;width:300px;font-size:11px;letter-spacing:.5px;line-height:12px}
.intro-text p{margin-bottom:11px}
.intro-text p.gap{margin-top:16px}
.signoff{left:390px;top:518px;font-family:"Great Vibes",cursive;font-size:21px;color:var(--ink)}
.intro-photo{left:640px;top:352px;width:378px;height:251px;background:linear-gradient(120deg,#8db0dd 0%,#b7a98a 35%,#5a3b3a 55%,#2a2526 80%,#1c1a1b 100%)}

.offers{left:182px;top:639px;width:887px;height:310px;background:var(--brown)}
.offer{top:0;width:250px;height:310px;text-align:center;color:var(--white)}
.offer-icon{position:absolute;left:95px;top:30px;width:60px;height:60px}
.offer-title{position:absolute;left:0;width:250px;top:108px;font-family:"Fira Sans Condensed",sans-serif;font-weight:300;font-size:21px;letter-spacing:1.5px}
.offer-rule{position:absolute;left:115px;top:137px;width:20px;height:1px;background:var(--teal)}
.offer-text{position:absolute;left:31px;top:172px;width:188px;text-align:left;font-size:10.5px;letter-spacing:.5px;line-height:11.5px}
.btn{position:absolute;border:1px solid var(--teal);color:var(--white);font-family:"Fira Sans Condensed",sans-serif;font-size:10px;display:flex;align-items:center;gap:12px;padding-left:9px}
.offer .btn{top:250px;width:88px;height:24px}

.contact{left:182px;top:949px;width:887px;height:194px;background:var(--paper)}
.contact-photo{left:233px;top:995px;width:103px;height:117px;background:linear-gradient(180deg,#a9c4e4 0%,#9aa58a 45%,#27304a 75%,#22283c 100%)}
.contact-role{left:419px;top:964px;font-family:"Fira Sans Condensed",sans-serif;font-size:18px;color:var(--teal)}
.contact-phone{left:420px;top:991px;font-family:"Fira Sans Condensed",sans-serif;font-size:17px;color:var(--black)}
.contact-address{left:420px;top:1020px;font-size:11px;line-height:11.7px;letter-spacing:.4px}
.contact-mail{left:420px;top:1066px;font-size:11px;letter-spacing:.5px}
.contact .btn,.contact-btn{left:421px;top:1090px;width:95px;height:24px;color:var(--teal);font-size:7.5px;gap:6px;padding-left:5px;border-width:1.5px}
.map{left:672px;top:970px;width:203px;height:135px;background:linear-gradient(90deg,#d8ebd5 0%,#bfd8ee 22%,#ececec 38%,#f3f3f3 100%)}

.footer{left:182px;top:1143px;width:887px;height:57px;background:var(--black);color:var(--white);font-family:"Fira Sans Condensed",sans-serif;font-size:8.5px;text-align:center;padding-top:15px;line-height:16px}
.footer a{color:var(--white);text-decoration:none;margin:0 3px}
</style>
</head>
<body>

<aside class="sidebar abs">
  <div class="brand abs">
    <span class="brand-name">Wiesen erleben</span>
    <span class="brand-tag">REITTHERAPIE</span>
  </div>
  <ul class="nav abs">
    <li>Reittherapie</li>
    <li>Angebot</li>
    <li>Über mich</li>
    <li>Pferde</li>
    <li>Kontakt</li>
  </ul>
</aside>

<header>
  <div class="hero abs" role="img" aria-label="Foto: Reiterin liegt entspannt auf dem Rücken eines schwarz-weissen Pferdes auf dem Sandplatz, Felder und Himmel im Hintergrund"></div>
  <h1 class="hero-title abs">Reittherapie</h1>
  <div class="hero-rule abs"></div>
  <p class="hero-sub abs">Beziehung zwischen Mensch und Pferd</p>
</header>

<section class="intro abs"></section>
<div class="intro-text abs">
  <p>In entspannter Atmosphäre dem Pferd begegnen.</p>
  <p>Freude, Motivation und Erfolgsmomente erfahren.</p>
  <p>Entspannung und Ruhe in der Natur finden.</p>
  <p>All das möchte ich meinen Klienten bieten und mit auf den Weg geben.</p>
  <p class="gap">Hab den Mut Dich zu melden!</p>
</div>
<p class="signoff abs">Ich freue mich auf Dich!</p>
<div class="intro-photo abs" role="img" aria-label="Foto: Reiterin mit Helm streichelt den Kopf eines schwarz-weissen Pferdes"></div>

<section class="offers abs">
  <div class="offer abs" style="left:70px">
    <svg class="offer-icon" viewBox="0 0 60 60" fill="none" stroke="#fff" stroke-width="1.2" role="img" aria-label="Personen-Symbol">
      <circle cx="30" cy="13" r="11"/>
      <path d="M25 16 q5 4 10 0"/>
      <path d="M3 58 a27 27 0 0 1 54 0 z"/>
    </svg>
    <h2 class="offer-title">Erstgespräch</h2>
    <div class="offer-rule"></div>
    <p class="offer-text">Ein Erstgespräch vor dem Besuch der Reittherapie klärt viele offene Fragen.</p>
    <span class="btn" style="left:72px">&gt; <span>MEHR DAZU</span></span>
  </div>
  <div class="offer abs" style="left:319px">
    <div class="offer-icon" style="border-radius:50%;background:rgba(255,255,255,.14)" role="img" aria-label="Symbol: Pferdekopf"></div>
    <h2 class="offer-title">Schnupperstunde</h2>
    <div class="offer-rule"></div>
    <p class="offer-text">Die Schnupperstunde ist dafür da, mich, die Pferde und die Stallumgebung kennen zu lernen.</p>
    <span class="btn" style="left:71px">&gt; <span>MEHR DAZU</span></span>
  </div>
  <div class="offer abs" style="left:577px">
    <div class="offer-icon" style="border-radius:50%;background:rgba(255,255,255,.14)" role="img" aria-label="Symbol: Reiter auf Pferd"></div>
    <h2 class="offer-title">Einzelstunde</h2>
    <div class="offer-rule"></div>
    <p class="offer-text">In der Einzelstunde wird an den gemeinsamen formulierten Förderzielen und Wünschen Schritt für Schritt gearbeitet.</p>
    <span class="btn" style="left:80px">&gt; <span>MEHR DAZU</span></span>
  </div>
</section>

<section class="contact abs"></section>
<div class="contact-photo abs" role="img" aria-label="Foto: Porträt der Reittherapeutin mit Pferd"></div>
<h3 class="contact-role abs">Reittherapeutin</h3>
<p class="contact-phone abs">0041 79 000 12 34</p>
<p class="contact-address abs">Lena Brunner<br>Wiesenweg 4<br>8460 Talheim</p>
<p class="contact-mail abs">info@wiesen-erleben.ch</p>
<span class="btn contact-btn">&gt; <span>KONTAKT AUFNEHMEN</span></span>
<div class="map abs" role="img" aria-label="Karte mit Standort des Hofes"></div>

<footer class="footer abs">
  <a>ZAHLUNGSBEDINGUNGEN</a><br>
  <a>IMPRESSUM</a><a>DATENSCHUTZ</a><a>SITEMAP</a>
</footer>

</body>
</html>
```